Business Card Design

I need a business card design. I am a sole practitioner.I am a psychotherapist and I need a professional card. I am also an art therapist (a form of psychotherapy using art) so I want the image to be professional/creative/maybe ethnic. I do not want a boring minimalist "medical" image, nor do I want it too hippy/tree hugging.
Colours like reds/ochres/yellows would be good.
Industry/Entity Type
Business
Contact Information for Business Card
Mira Tanvel
Psychotherapy, Counselling and Art Therapy
Korrabel Lodge Counselling and Wellbeing services
17 Farrow Lane, Pelbury 4091
0419362750 www.MiraTanvel.com.au
on rear of card I need the option to have at least 4 or 5 appointment times /dates
Look and feel
Each slider illustrates characteristics of the customer's brand and the style your logo design should communicate.

```html
<!DOCTYPE html>
<html lang="en">
<head>
<meta charset="utf-8">
<title>Mira Tanvel – Business Card</title>
<link rel="stylesheet" href="https://fonts.googleapis.com/css2?family=Cinzel:wght@400;600&display=swap">
<style>
  :root {
    --page: #ffffff;
    --ochre-deep: #d9a42c;
    --ochre: #e9c25a;
    --ochre-pale: #f1deaa;
    --paper: #efece1;
    --ink: #9a2f2a;
  }
  * { box-sizing: border-box; margin: 0; padding: 0; }
  html, body {
    width: 1200px; height: 1134px; overflow: hidden;
    background: var(--page);
    font-family: "Cinzel", serif;
    color: var(--ink);
  }
  .card {
    position: absolute; left: 330px;
    width: 560px; height: 320px;
    box-shadow: 0 1px 3px rgba(0,0,0,0.12);
  }
  .card-front {
    top: 160px;
    background: linear-gradient(115deg, var(--ochre-deep) 0%, var(--ochre) 48%, var(--ochre-pale) 62%, var(--paper) 74%);
  }
  .card-back {
    top: 640px;
    background: linear-gradient(90deg, var(--ochre) 0%, var(--ochre-pale) 42%, var(--paper) 55%, var(--paper) 100%);
  }
  .brand-mark {
    position: absolute; left: 40px; top: 58px;
    display: flex; align-items: center; gap: 8px;
    font-size: 15px; font-weight: 600; letter-spacing: 1px;
  }
  .brand-mark .square { width: 14px; height: 14px; background: var(--ink); }
  .identity { position: absolute; right: 40px; top: 92px; text-align: center; width: 270px; }
  .identity .name { font-size: 17px; letter-spacing: 2px; margin-bottom: 8px; }
  .identity .services { font-size: 11.5px; letter-spacing: 1px; line-height: 1.3; }
  .practice {
    position: absolute; left: 34px; top: 222px; width: 250px;
    font-size: 10.5px; line-height: 1.45; text-align: center; letter-spacing: 0.5px;
  }
  .divider { position: absolute; left: 300px; top: 210px; width: 2px; height: 78px; background: var(--ink); }
  .contact {
    position: absolute; left: 350px; top: 262px;
    font-size: 10.5px; line-height: 1.5; letter-spacing: 1px;
  }
  .back-title {
    position: absolute; left: 0; right: 0; top: 42px; text-align: center;
    font-size: 15px; letter-spacing: 1.5px;
  }
  .slots { position: absolute; top: 92px; left: 60px; right: 40px; display: flex; gap: 40px; }
  .slot-column { flex: 1; display: flex; flex-direction: column; gap: 18px; }
  .slot { display: flex; align-items: flex-end; gap: 8px; font-size: 12px; letter-spacing: 1px; }
  .slot .line { flex: 1; border-bottom: 1px solid var(--ink); height: 12px; }
</style>
</head>
<body>
  <section class="card card-front">
    <div class="brand-mark"><span class="square"></span>Mira Tanvel</div>
    <div class="identity">
      <p class="name">Mira Tanvel</p>
      <p class="services">Psychotherapy, Counselling &amp;<br>Art Therapy</p>
    </div>
    <div class="practice">
      Korrabel Lodge Counselling &amp; Wellbeing Services<br>
      17 Farrow Lane, Pelbury 4091
    </div>
    <div class="divider"></div>
    <div class="contact">
      Tel : 0419 362750<br>
      www.MiraTanvel.com.au
    </div>
  </section>

  <section class="card card-back">
    <h2 class="back-title">Appointment Details</h2>
    <div class="slots">
      <div class="slot-column">
        <div class="slot">Date<span class="line"></span></div>
        <div class="slot">Date<span class="line"></span></div>
        <div class="slot">Date<span class="line"></span></div>
        <div class="slot">Date<span class="line"></span></div>
        <div class="slot">Date<span class="line"></span></div>
      </div>
      <div class="slot-column">
        <div class="slot">Time<span class="line"></span></div>
        <div class="slot">Time<span class="line"></span></div>
        <div class="slot">Time<span class="line"></span></div>
        <div class="slot">Time<span class="line"></span></div>
        <div class="slot">Time<span class="line"></span></div>
      </div>
    </div>
  </section>
</body>
</html>
```